Amber Lantern Cafe Business Card

We need a business card design for a new European Cafe. Main menu will be coffee and deserts.

Requirements
Must have
• Logo - 1 of the attached versions
Address - TBA (you can use 487 Morrow Ave Unit 9 for now)
Phone - TBA (you can use 555-238-4176 for now)

```html
<!DOCTYPE html>
<html lang="en">
<head>
<meta charset="utf-8">
<title>Amber Lantern Cafe Business Card</title>
<link rel="stylesheet" href="https://fonts.googleapis.com/css2?family=PT+Sans+Narrow:wght@400;700&display=swap">
<style>
  :root {
    --page: #ece7df;
    --bark: #6b5c4a;
    --bark-light: #7b6a55;
    --cream: #f7ebda;
    --cream-text: #f3e6d3;
    --ink: #6b5c4a;
  }
  * { margin: 0; padding: 0; box-sizing: border-box; }
  html, body { width: 1200px; height: 1000px; overflow: hidden; }
  body {
    position: relative;
    background: var(--page);
    font-family: "PT Sans Narrow", "Arial Narrow", sans-serif;
  }
  .card {
    position: absolute;
    left: 83px;
    width: 628px;
    height: 349px;
    overflow: hidden;
    background: var(--bark);
    box-shadow: 2px 3px 6px rgba(0,0,0,0.35);
  }
  .card--front { top: 78px; }
  .card--back { top: 555px; }
  .swirl-area {
    position: absolute;
    inset: 0;
    background: radial-gradient(ellipse at 62% 55%, var(--bark-light) 0%, var(--bark) 45%, var(--bark-light) 70%, var(--bark) 100%);
  }
  /* front */
  .front-band {
    position: absolute;
    left: 0; right: 0;
    top: 90px; height: 170px;
    background: var(--cream);
    box-shadow: 0 3px 4px rgba(0,0,0,0.25);
    display: flex;
    align-items: center;
    justify-content: center;
    gap: 18px;
  }
  .brand-square {
    width: 95px; height: 95px;
    background: var(--ink);
    border-radius: 4px;
    flex: none;
  }
  .brand-name {
    font-size: 40px;
    font-weight: 400;
    color: var(--ink);
    white-space: nowrap;
  }
  .web {
    position: absolute;
    left: 226px; top: 292px;
    display: flex; align-items: center; gap: 6px;
    color: var(--cream-text);
    font-size: 16px;
  }
  /* back */
  .back-strip {
    position: absolute;
    left: 33px; top: 0; bottom: 0;
    width: 204px;
    background: var(--cream);
    box-shadow: 3px 0 4px rgba(0,0,0,0.3);
    display: flex; flex-direction: column;
    align-items: center;
    padding-top: 129px;
    gap: 16px;
  }
  .back-strip .brand-square { width: 60px; height: 60px; }
  .back-strip .brand-name { font-size: 22px; }
  .contact {
    position: absolute;
    left: 297px; top: 86px;
    color: var(--cream-text);
  }
  .contact__name { font-size: 30px; font-weight: 400; margin-bottom: 14px; }
  .contact__row {
    display: flex; align-items: flex-start; gap: 16px;
    font-size: 16px; line-height: 24px;
    margin-bottom: 12px;
  }
  .contact__row svg { flex: none; width: 20px; height: 22px; margin-top: 1px; }
</style>
</head>
<body>

<section class="card card--front">
  <div class="swirl-area" role="img" aria-label="Large soft swirl pattern in two brown tones"></div>
  <div class="front-band">
    <div class="brand-square"></div>
    <span class="brand-name">Amber Lantern Cafe</span>
  </div>
  <div class="web">
    <svg width="20" height="20" viewBox="0 0 20 20" fill="none" stroke="currentColor" stroke-width="1.3">
      <circle cx="10" cy="10" r="8.5"/>
      <ellipse cx="10" cy="10" rx="4" ry="8.5"/>
      <line x1="1.5" y1="10" x2="18.5" y2="10"/>
      <path d="M3 5.5h14M3 14.5h14"/>
    </svg>
    <span>www.amberlanterncafe.com</span>
  </div>
</section>

<section class="card card--back">
  <div class="swirl-area" role="img" aria-label="Large soft swirl pattern in two brown tones"></div>
  <div class="back-strip">
    <div class="brand-square"></div>
    <span class="brand-name">Amber Lantern Cafe</span>
  </div>
  <div class="contact">
    <h1 class="contact__name">Mara Ellison</h1>
    <div class="contact__row">
      <svg viewBox="0 0 20 22" fill="currentColor">
        <rect x="5" y="1" width="10" height="20" rx="1.5"/>
        <rect x="7" y="4" width="6" height="5" fill="var(--bark)"/>
        <rect x="7" y="11" width="2" height="2" fill="var(--bark)"/>
        <rect x="11" y="11" width="2" height="2" fill="var(--bark)"/>
        <rect x="7" y="15" width="2" height="2" fill="var(--bark)"/>
        <rect x="11" y="15" width="2" height="2" fill="var(--bark)"/>
      </svg>
      <span>555-238-4176</span>
    </div>
    <div class="contact__row">
      <svg viewBox="0 0 20 22" fill="currentColor">
        <path d="M10 1a7 7 0 0 0-7 7c0 5 7 13 7 13s7-8 7-13a7 7 0 0 0-7-7z"/>
        <circle cx="10" cy="8" r="2.6" fill="var(--bark)"/>
      </svg>
      <span>N. 45d 31.12 W. 122.40.36</span>
    </div>
    <div class="contact__row">
      <svg viewBox="0 0 20 22" fill="currentColor">
        <path d="M10 2 1 11h3v9h12v-9h3z"/>
        <rect x="8" y="13" width="4" height="7" fill="var(--bark)"/>
      </svg>
      <span>487 Morrow Ave Unit 9<br>Larkfield, Oregon, United States, 97001</span>
    </div>
  </div>
</section>

</body>
</html>
```